COMMERCIAL OFFICE FOR SALE- Brochure, Miami, FL 33131

BROCHURE DESIGN BRIEF – COMMERCIAL OFFICE FOR SALE

I need a clean, modern brochure for a commercial office listing (FOR SALE, not lease). This will be used both digitally (email + SpanDesk/attachments) and printed if needed.

Please follow a “Sample Flyer Copy” style layout — strong headline, clean sections, minimal clutter, and easy to scan. Use fints Seasons and Poppins interchangeably.

All property details, specs, and exact wording should be pulled directly from the MLS Listing file I provided. Do not guess or rewrite specs.

OVERALL LOOK + FEEL

Clean, high-end, professional (Brickell / financial district vibe)

Think: simple, sharp, not busy

Neutral palette (white, black, soft gray) + subtle accent color if needed

Prioritize readability over design gimmicks

Plenty of white space

FORMAT

1-page flyer (primary)

Also format so it can easily convert into a 2-page version if needed

PDF optimized for email + print

HEADER SECTION (TOP OF PAGE)

Large, strong headline:

Example: “Office Condo for Sale | Brickell” (adjust based on MLS info)

Subheadline (smaller):

Key positioning (corner unit, square footage, etc.)

Include 1 strong hero image (best photo of the unit)

PROPERTY OVERVIEW (RIGHT UNDER HEADER OR NEXT BLOCK)

Clean bullet section with icons if possible:

Include:

Total square footage

Layout highlights (conference room, offices, open workspace, etc.)

Kitchen / breakroom

Reception area

Storage / printer room

Floor or suite number

Any standout feature (corner unit, natural light, views, etc.)

Keep this tight and clean — no long paragraphs.

PRICING SECTION

Clearly state: FOR SALE

Price (from MLS)

Price per square foot

Make this visually stand out.

LOCATION SECTION

Short and clean:

Building name + address

1–2 lines max on location advantages (Brickell, access, etc.)

Optional small map if it fits cleanly

ADDITIONAL DETAILS (IF SPACE ALLOWS)

Building amenities (if relevant)

Parking info

Zoning / permitted uses (if applicable)

Only include what is confirmed in MLS.

IMAGES

3–5 total max

Keep it clean — do not overcrowd

Prioritize:

Main workspace

Conference room

Kitchen

Any standout feature

CONTACT SECTION (VERY IMPORTANT – EXACT FORMAT)

This must be clean and prominent.

Colette Varnum
REALTOR®
Tamsworth Lindale HomePartners QRF Realty

Phone: [your number]
Email: [your email]

Call to action line:

“For more information or to schedule a private showing, contact Colette Varnum.”

Include my business card details (office location etc.) in this section.

BROKERAGE + LOGOS

Use TLHP QRF Realty logos provided

Place cleanly (bottom or footer)

Do not distort or restyle logos

FOOTER

Standard disclaimer if needed

Keep minimal

IMPORTANT NOTES

This is a SALE listing — do not use the word lease anywhere

Do not overdesign — clean always wins

Keep everything aligned and balanced

Make sure spacing feels high-end, not cramped
Updates

Please include this video link within the document: https://vidshare.example/kQ7pTzR2vNa?ref=hx4Lm9Ys_Wd2Pc8E

State: Step inside. Watch the full video tour. and hyperlink Watch with the link

Target Market(s)

Buyers, Professionals, Lawyer Office, Family Office, Small FInancial Offices

Industry/Entity Type

Commercial Real Estate

Font styles to use
Serif
Sans Serif

Requirements
Must have
• Clean, clear, layout and good imagery
Should not have
• Professional flow, follow my font guidlines and thebrochure i shared as a guide

```html
<!DOCTYPE html>
<html lang="en">
<head>
<meta charset="utf-8">
<title>Office Condo for Sale – Brickell</title>
<link href="https://fonts.googleapis.com/css2?family=Roboto:wght@400;500;700;900&display=swap" rel="stylesheet">
<style>
  :root {
    --blue: #4a93e0;
    --blue-deep: #2b7fd6;
    --blue-pale: #cfe3f7;
    --ink: #1a1a1a;
    --gray: #666a6e;
    --gray-box: #e6e7e8;
    --white: #ffffff;
  }
  * { box-sizing: border-box; margin: 0; padding: 0; }
  html, body { width: 927px; height: 1200px; overflow: hidden; background: var(--white); }
  body { font-family: "Roboto", Arial, sans-serif; color: var(--ink); }
  .flyer { position: relative; width: 927px; height: 1200px; overflow: hidden; }

  .headline {
    position: absolute; left: 0; top: 0; width: 523px; height: 151px;
    background: var(--blue); color: var(--white);
    display: flex; align-items: center; justify-content: center; text-align: center;
    font-size: 43px; font-weight: 400; line-height: 1.18;
  }
  .hero-photo {
    position: absolute; left: 523px; top: 0; width: 404px; height: 583px;
    background: linear-gradient(180deg, #7fb2e8 0%, #4f7fb8 35%, #2d4f7a 70%, #3f6a3c 92%, #6d8a5a 100%);
  }

  .subhead {
    position: absolute; left: 15px; top: 180px; padding-left: 10px;
    border-left: 4px solid var(--blue);
    color: var(--blue-deep); font-size: 26px; font-weight: 700; line-height: 1.3;
  }
  .video-note {
    position: absolute; left: 15px; top: 264px; width: 505px;
    font-size: 18px; line-height: 1.3; color: var(--ink);
  }
  .video-note a { color: var(--ink); text-decoration: none; }

  .overview {
    position: absolute; left: 0; top: 330px; width: 523px; height: 247px;
    background: var(--blue-pale); padding: 9px 14px 0 15px;
  }
  .overview li {
    list-style: none; display: flex; align-items: flex-start; gap: 9px;
    font-size: 17px; line-height: 23.5px;
  }
  .overview svg { flex: none; margin-top: 5px; }

  .pricing { position: absolute; left: 0; top: 600px; width: 415px; text-align: center; }
  .pricing .label { font-size: 42px; font-weight: 900; letter-spacing: 3px; color: var(--gray); line-height: 1.1; }
  .pricing .price { font-size: 41px; font-weight: 700; color: var(--blue-deep); line-height: 1.1; }
  .pricing .per-sf { font-size: 18px; margin-top: 6px; }

  .location {
    position: absolute; left: 18px; top: 730px; width: 383px; height: 126px;
    background: var(--gray-box); padding: 10px 11px; font-size: 15.5px; line-height: 1.3;
  }
  .location strong { display: block; font-weight: 700; }

  .details { position: absolute; left: 27px; top: 870px; width: 385px; font-size: 16.5px; line-height: 1.3; }
  .details .row { display: flex; margin-bottom: 7px; }
  .details dt { width: 106px; flex: none; font-weight: 700; }

  .gallery { position: absolute; left: 415px; top: 588px; width: 512px; height: 512px; }
  .shot { position: absolute; }
  .shot.kitchen { left: 0; top: 0; width: 247px; height: 165px; background: linear-gradient(160deg, #c9d3da, #a89a86 60%, #6c6a66); }
  .shot.open-office { left: 255px; top: 0; width: 257px; height: 165px; background: linear-gradient(170deg, #eef0f0, #cfd2d2 60%, #8d9396); }
  .shot.conference { left: 0; top: 172px; width: 247px; height: 167px; background: linear-gradient(170deg, #f1efe9, #d8d3c8 55%, #7f8285); }
  .shot.private-office { left: 255px; top: 172px; width: 257px; height: 167px; background: linear-gradient(170deg, #f2efe8, #dcd6ca 55%, #808488); }
  .shot.entry { left: 0; top: 347px; width: 247px; height: 165px; background: linear-gradient(170deg, #e9e2d6, #b9a98f 55%, #6f6a62); }
  .shot.corridor { left: 255px; top: 347px; width: 257px; height: 165px; background: linear-gradient(170deg, #ece8e1, #b89a7a 55%, #5c5e60); }

  .footer {
    position: absolute; left: 0; top: 1112px; width: 927px; height: 88px;
    background: var(--blue); color: var(--white); display: flex; align-items: center;
  }
  .brokerage {
    width: 235px; padding-left: 12px; font-size: 13px; font-weight: 700; line-height: 1.25;
    letter-spacing: 0.5px; text-transform: uppercase; display: flex; align-items: center; gap: 8px;
  }
  .brokerage .mark { width: 10px; height: 10px; background: var(--white); flex: none; }
  .contact { flex: 1; text-align: center; padding-right: 20px; }
  .contact .cta { font-size: 17px; font-weight: 700; margin-bottom: 5px; }
  .contact p { font-size: 13.5px; line-height: 1.35; }
</style>
</head>
<body>
<main class="flyer">
  <h1 class="headline">Office Condo for Sale<br>Brickell</h1>
  <div class="hero-photo" role="img" aria-label="Glass office tower with a tall arched top against a blue sky, palm trees at its base"></div>

  <h2 class="subhead">2,146 SF Move-In Ready<br>Corner Suite</h2>
  <p class="video-note">Step inside. <a href="https://vidshare.example/kQ7pTzR2vNa?ref=hx4Lm9Ys_Wd2Pc8E">Watch</a> the full video tour:<br>https://vidshare.example/kQ7pTzR2vNa?ref=hx4Lm9Ys_Wd2Pc8E</p>

  <ul class="overview">
    <li><svg width="12" height="12" viewBox="0 0 12 12"><rect width="12" height="12" fill="#2b6cb0"/><path d="M2.5 6.2l2.3 2.3 4.7-5" stroke="#fff" stroke-width="1.8" fill="none"/></svg>2,146 SF private office suite</li>
    <li><svg width="12" height="12" viewBox="0 0 12 12"><rect width="12" height="12" fill="#2b6cb0"/><path d="M2.5 6.2l2.3 2.3 4.7-5" stroke="#fff" stroke-width="1.8" fill="none"/></svg>Four private offices</li>
    <li><svg width="12" height="12" viewBox="0 0 12 12"><rect width="12" height="12" fill="#2b6cb0"/><path d="M2.5 6.2l2.3 2.3 4.7-5" stroke="#fff" stroke-width="1.8" fill="none"/></svg>Conference room</li>
    <li><svg width="12" height="12" viewBox="0 0 12 12"><rect width="12" height="12" fill="#2b6cb0"/><path d="M2.5 6.2l2.3 2.3 4.7-5" stroke="#fff" stroke-width="1.8" fill="none"/></svg>Reception area</li>
    <li><svg width="12" height="12" viewBox="0 0 12 12"><rect width="12" height="12" fill="#2b6cb0"/><path d="M2.5 6.2l2.3 2.3 4.7-5" stroke="#fff" stroke-width="1.8" fill="none"/></svg>Printer / copy room</li>
    <li><svg width="12" height="12" viewBox="0 0 12 12"><rect width="12" height="12" fill="#2b6cb0"/><path d="M2.5 6.2l2.3 2.3 4.7-5" stroke="#fff" stroke-width="1.8" fill="none"/></svg>Kitchenette</li>
    <li><svg width="12" height="12" viewBox="0 0 12 12"><rect width="12" height="12" fill="#2b6cb0"/><path d="M2.5 6.2l2.3 2.3 4.7-5" stroke="#fff" stroke-width="1.8" fill="none"/></svg><span>Corner unit overlooking planned garden pavilion<br>&amp; Lumo by Casa Verin</span></li>
    <li><svg width="12" height="12" viewBox="0 0 12 12"><rect width="12" height="12" fill="#2b6cb0"/><path d="M2.5 6.2l2.3 2.3 4.7-5" stroke="#fff" stroke-width="1.8" fill="none"/></svg>Carpeted floors, smoke detectors, sprinklers</li>
    <li><svg width="12" height="12" viewBox="0 0 12 12"><rect width="12" height="12" fill="#2b6cb0"/><path d="M2.5 6.2l2.3 2.3 4.7-5" stroke="#fff" stroke-width="1.8" fill="none"/></svg>Common, covered &amp; guest parking</li>
  </ul>

  <section class="pricing">
    <div class="label">FOR SALE</div>
    <div class="price">$1,025,000</div>
    <div class="per-sf">Price per SF: approx. $477.60/SF</div>
  </section>

  <section class="location">
    <strong>1480 Brickell Ave #505 B, Miami, FL 33131</strong>
    Prime Brickell Avenue &amp; Coral Way location. Steps from Harbor Row Village and Bayline City Centre.
  </section>

  <dl class="details">
    <div class="row"><dt>Building:</dt><dd>20 story building (1982), Office Space / Professional, Zoning x6407, Corporate Office last use, Central A/C, Security guard</dd></div>
    <div class="row"><dt>Association:</dt><dd>$3,545 monthly (A/C &amp; heating maintenance, interior electric, insurance, janitorial, trash removal)</dd></div>
    <div class="row"><dt>Parking:</dt><dd>Common, covered, guest</dd></div>
  </dl>

  <section class="gallery">
    <div class="shot kitchen" role="img" aria-label="Kitchenette with wood cabinets, counter stools and window"></div>
    <div class="shot open-office" role="img" aria-label="Open carpeted workspace with ceiling lights"></div>
    <div class="shot conference" role="img" aria-label="Conference room with wooden table and window view"></div>
    <div class="shot private-office" role="img" aria-label="Private office with desk and chair by a window"></div>
    <div class="shot entry" role="img" aria-label="Glass double doors opening into the suite"></div>
    <div class="shot corridor" role="img" aria-label="Building corridor leading to the wooden suite entrance"></div>
  </section>

  <footer class="footer">
    <div class="brokerage"><span class="mark"></span><span>Tamsworth Lindale HomePartners QRF Realty</span></div>
    <div class="contact">
      <div class="cta">For more information or to schedule a private showing, contact Colette Varnum.</div>
      <p>Phone: 305 555 0147 &nbsp;Email: colettevarnum@mailbox.example WWW: colettevarnumqrf.example</p>
      <p>Office Address: 720 Palmetto Way, Coral Gables, FL 33146 C:305.555.0147</p>
    </div>
  </footer>
</main>
</body>
</html>
```